Business card for Financial Technology company

Hello! We'd like to create business cards for 4 members of our company. Our company is a financial technology business that provides funding for businesses. We want to give it a VC (venture captal) look and feel. Clean, fresh and minimal but with a flair of artistry. I'll include some samples of cards we like. It would be great if the back of the card was artistic (see sample files 1 and 2) and the front of the card was the business info. The name of the company is Q8 Funding.

```html
<!DOCTYPE html>
<html lang="en">
<head>
<meta charset="utf-8">
<title>Q8 Funding — Business Cards</title>
<link rel="stylesheet" href="https://fonts.googleapis.com/css2?family=Lato:wght@400;700;900&display=swap">
<style>
  :root {
    --backdrop: #2b2c2f;
    --card-white: #ffffff;
    --card-black: #1b1b1c;
    --ink: #1a1a1a;
    --ink-soft: #555555;
    --rule: #b9b9b9;
    --green: #3aa84a;
    --yellow: #fcd20f;
    --orange: #f7931e;
    --pink: #e7208a;
    --purple: #6a2c91;
    --navy: #283a8f;
    --sky: #29a8e0;
    --teal: #117a6a;
  }
  * { box-sizing: border-box; margin: 0; padding: 0; }
  html, body { width: 1200px; height: 952px; overflow: hidden; }
  body {
    background: var(--backdrop);
    font-family: "Lato", sans-serif;
    color: var(--ink);
    position: relative;
  }

  /* Front: contact card (portrait) */
  .card-front {
    position: absolute;
    left: 150px; top: 186px;
    width: 340px; height: 580px;
    background: var(--card-white);
    box-shadow: 0 14px 34px rgba(0,0,0,.45);
    display: flex; flex-direction: column; align-items: center;
    padding: 96px 34px 0;
    text-align: center;
  }
  .brand-mark {
    display: flex; align-items: center; gap: 10px;
    margin-bottom: 54px;
  }
  .brand-mark__dot {
    width: 14px; height: 14px;
    background: var(--pink);
  }
  .brand-mark__name {
    font-family: "Lato", sans-serif;
    font-weight: 700;
    font-size: 22px;
    letter-spacing: 3px;
    text-transform: uppercase;
    color: var(--ink);
  }
  .person-name {
    font-weight: 900;
    font-size: 19px;
    letter-spacing: .5px;
    text-transform: uppercase;
  }
  .person-role {
    font-size: 12px;
    color: var(--ink-soft);
    margin-top: 3px;
  }
  .divider {
    width: 100%;
    height: 1px;
    background: var(--rule);
    margin: 16px 0;
  }
  .contact-icons { display: flex; gap: 6px; margin-bottom: 12px; }
  .contact-icons svg { width: 24px; height: 24px; display: block; }
  .contact-lines, .address { font-size: 13px; line-height: 1.55; color: #333; }
  .address { line-height: 1.45; }

  /* Back: art card (landscape) */
  .card-back {
    position: absolute;
    left: 570px; top: 186px;
    width: 520px; height: 310px;
    background: var(--card-black);
    box-shadow: 0 14px 34px rgba(0,0,0,.45);
    overflow: hidden;
  }
  .art-field {
    position: absolute;
    left: 0; top: 0;
    width: 100%; height: 100%;
    background:
      linear-gradient(120deg,
        var(--green) 0%, var(--teal) 22%, var(--navy) 42%,
        var(--purple) 58%, var(--pink) 74%, var(--orange) 88%, var(--yellow) 100%);
    opacity: .9;
    clip-path: polygon(0 0, 100% 0, 100% 46%, 0 70%);
  }
  .back-name {
    position: absolute;
    left: 40px; bottom: 40px;
    font-family: "Lato", sans-serif;
    font-weight: 700;
    font-size: 20px;
    letter-spacing: 4px;
    text-transform: uppercase;
    color: #ffffff;
  }
</style>
</head>
<body>

  <section class="card-front" aria-label="Business card front">
    <div class="brand-mark">
      <span class="brand-mark__dot"></span>
      <span class="brand-mark__name">Q8 Funding</span>
    </div>

    <h1 class="person-name">Daniel R. Whitmore</h1>
    <p class="person-role">Managing Director</p>

    <div class="divider"></div>

    <div class="contact-icons">
      <svg viewBox="0 0 24 24" aria-label="Phone">
        <rect width="24" height="24" rx="3" fill="var(--sky)"/>
        <path d="M8 6c1 0 1.6 2.2 1.6 2.8S8.6 10 8.6 10c.8 1.9 2.4 3.5 4.4 4.4 0 0 .6-1 1.2-1s2.8.6 2.8 1.6-1 2-2 2C10 17 7 14 7 9c0-1 .2-3 1-3z" fill="#fff"/>
      </svg>
      <svg viewBox="0 0 24 24" aria-label="Email">
        <rect width="24" height="24" rx="3" fill="var(--purple)"/>
        <rect x="5" y="7.5" width="14" height="9" fill="none" stroke="#fff" stroke-width="1.5"/>
        <path d="M5 7.5l7 5.5 7-5.5" fill="none" stroke="#fff" stroke-width="1.5"/>
      </svg>
      <svg viewBox="0 0 24 24" aria-label="Website">
        <rect width="24" height="24" rx="3" fill="var(--pink)"/>
        <circle cx="12" cy="12" r="6.5" fill="none" stroke="#fff" stroke-width="1.4"/>
        <ellipse cx="12" cy="12" rx="3" ry="6.5" fill="none" stroke="#fff" stroke-width="1.2"/>
        <path d="M5.5 12h13M6.5 9h11M6.5 15h11" stroke="#fff" stroke-width="1.1"/>
      </svg>
    </div>

    <p class="contact-lines">
      +00 321 654 87<br>
      hello@q8funding.com<br>
      www.q8funding.com
    </p>

    <div class="divider"></div>

    <p class="address">
      1270 Harbor Point Avenue<br>
      Boston, MA 02110
    </p>

    <div class="divider"></div>
  </section>

  <section class="card-back" aria-label="Business card back">
    <div class="art-field" role="img" aria-label="Abstract faceted colour field in green, blue, purple, pink and yellow"></div>
    <p class="back-name">Q8 Funding</p>
  </section>

</body>
</html>
```